Brochure design - Ventoro Rideshare community

We need a print ready brochure to tell drivers about the Ventoro community and the benefits of being a driver. We offer a alternative product to zappo and give drivers the ability to build their own customer base and build passive income. see design brief. check out our website www.ventoro-example.travel put in some good pics. Wanting a A4 Double sided brochure

Target Market(s)

Rideshare Drivers

Industry/Entity Type

Community

Font styles to use
Serif

Colors
00a990

Requirements
Must have
• clean design look. not too busy

```html
<!DOCTYPE html>
<html lang="en">
<head>
<meta charset="utf-8">
<title>Ventoro Rideshare – Driver Brochure</title>
<link rel="stylesheet" href="https://fonts.googleapis.com/css2?family=Open+Sans:wght@400;600;700;800&display=swap">
<style>
  :root {
    --lime: #8dc63f;
    --lime-soft: #cfe6a6;
    --blue: #2a66b0;
    --blue-deep: #1d4d8c;
    --ink: #333c44;
    --ink-soft: #5b646c;
    --paper: #ffffff;
    --stage: #ececec;
    --photo-dark: #3a3f46;
    --photo-light: #d7dbe0;
    --band-orange: #f0892a;
    --band-red: #e2342d;
    --band-green: #6fb83a;
  }
  * { box-sizing: border-box; margin: 0; padding: 0; }
  html, body {
    width: 802px; height: 1200px; overflow: hidden;
    background: var(--stage);
    font-family: "Open Sans", Arial, sans-serif;
    color: var(--ink);
  }
  .spread {
    position: absolute; left: 41px; width: 720px; height: 500px;
    display: flex; background: var(--paper);
    box-shadow: 0 2px 10px rgba(0,0,0,.12);
  }
  .spread--outer { top: 60px; }
  .spread--inner { top: 640px; }
  .page { position: relative; width: 360px; height: 500px; overflow: hidden; }
  .page + .page { border-left: 1px solid #e2e2e2; }
  .page-art { position: absolute; inset: 0; width: 100%; height: 100%; }

  /* Back cover */
  .back-title {
    position: absolute; top: 28px; left: 0; right: 0; text-align: center;
    font-size: 21px; font-weight: 700; line-height: 1.2; color: var(--ink);
  }
  .back-photo {
    position: absolute; top: 90px; left: 40px; width: 280px; height: 110px;
    border-radius: 6px;
    background: linear-gradient(180deg, var(--photo-light) 0%, var(--photo-dark) 55%, var(--photo-light) 100%);
  }
  .service-table {
    position: absolute; top: 214px; left: 70px; width: 220px;
    border-collapse: collapse; font-size: 8.5px;
  }
  .service-table th { background: var(--ink); color: #fff; text-align: left; padding: 3px 6px; font-weight: 600; }
  .service-table td { border-bottom: 1px solid #d6d6d6; padding: 3px 6px; }
  .back-copy {
    position: absolute; top: 292px; left: 50px; right: 50px; text-align: center;
    font-size: 9px; line-height: 1.45; color: var(--ink);
  }
  .back-copy p + p { margin-top: 8px; }
  .back-web {
    position: absolute; bottom: 38px; left: 0; right: 0; text-align: center;
    font-size: 13px; font-weight: 600; color: #fff; letter-spacing: .3px;
  }

  /* Front cover */
  .cover-photo { position: absolute; top: 0; left: 0; width: 360px; height: 200px; }
  .brand-name {
    position: absolute; top: 300px; right: 34px;
    font-size: 46px; font-weight: 700; color: var(--ink); line-height: 1;
  }

  /* Inside left */
  .benefits { position: absolute; top: 34px; left: 34px; right: 30px; list-style: none; }
  .benefit { position: relative; padding-left: 14px; margin-bottom: 12px; font-size: 9px; line-height: 1.4; }
  .benefit::before {
    content: ""; position: absolute; left: 0; top: 4px; width: 6px; height: 6px;
    background: var(--lime); border-radius: 50%;
  }
  .benefit-title { display: block; font-weight: 700; color: var(--ink); font-size: 10px; }
  .benefit-text { color: var(--ink-soft); }

  /* Inside right */
  .jobs-title { position: absolute; top: 30px; left: 26px; font-size: 19px; font-weight: 700; color: var(--blue); }
  .jobs-label { position: absolute; top: 62px; left: 28px; font-size: 9px; font-weight: 600; color: var(--lime); }
  .funnel { position: absolute; top: 80px; left: 26px; width: 190px; height: 200px; }
  .funnel text { font-family: "Open Sans", Arial, sans-serif; font-size: 8.5px; font-weight: 600; fill: #fff; }
  .people-figure {
    position: absolute; top: 150px; left: 226px; width: 110px; height: 160px;
    background: linear-gradient(180deg, #9aa0a6, #3e444a);
  }
  .referral {
    position: absolute; top: 320px; left: 100px; right: 24px; text-align: right;
    font-size: 14px; font-weight: 700; line-height: 1.25; color: var(--blue);
  }
  .referral span { display: block; }
  .referral strong { display: block; font-size: 20px; color: var(--blue-deep); }
  .referral-note {
    position: absolute; top: 396px; left: 26px; right: 24px;
    font-size: 8.5px; color: var(--ink-soft); line-height: 1.4;
  }
</style>
</head>
<body>

<section class="spread spread--outer">
  <article class="page page--back">
    <svg class="page-art" viewBox="0 0 360 500" preserveAspectRatio="none" aria-hidden="true">
      <defs>
        <linearGradient id="backSky" x1="0" y1="0" x2="0" y2="1">
          <stop offset="0" stop-color="#d9dcdf"/>
          <stop offset="1" stop-color="#ffffff"/>
        </linearGradient>
      </defs>
      <rect width="360" height="250" fill="url(#backSky)"/>
      <path d="M0 360 C120 330 240 340 360 300 L360 500 L0 500 Z" fill="var(--lime-soft)"/>
      <path d="M0 400 C130 370 250 380 360 340 L360 500 L0 500 Z" fill="var(--lime)"/>
    </svg>
    <h2 class="back-title">We offer clients a range<br>of services</h2>
    <div class="back-photo" role="img" aria-label="Photo of a black executive sedan"></div>
    <table class="service-table">
      <tr><th>Service</th><th>Best for</th></tr>
      <tr><td>Ventoro Rideshare</td><td>Everyday trips</td></tr>
      <tr><td>Ventoro Executive</td><td>Business travel</td></tr>
      <tr><td>Ventoro Maxi</td><td>Groups of six</td></tr>
    </table>
    <div class="back-copy">
      <p>It is free to join. Sign up as a driver and start building your own clients.</p>
      <p>Book your ride any time through the Ventoro app or our website.</p>
    </div>
    <p class="back-web">www.ventoro-example.travel</p>
  </article>

  <article class="page page--front">
    <svg class="page-art" viewBox="0 0 360 500" preserveAspectRatio="none" aria-hidden="true">
      <path d="M0 0 H360 V240 C250 270 120 230 0 210 Z" fill="var(--blue)"/>
      <path d="M0 0 H360 V222 C250 250 120 215 0 195 Z" fill="var(--lime)"/>
      <path d="M0 440 C120 470 240 430 360 420 L360 500 L0 500 Z" fill="var(--lime)"/>
    </svg>
    <svg class="cover-photo" viewBox="0 0 360 200" preserveAspectRatio="none" role="img" aria-label="Photo of a silver saloon car in motion">
      <defs>
        <linearGradient id="coverPhoto" x1="0" y1="0" x2="1" y2="1">
          <stop offset="0" stop-color="#e6e9ec"/>
          <stop offset=".55" stop-color="#a7adb3"/>
          <stop offset="1" stop-color="#5c636b"/>
        </linearGradient>
      </defs>
      <path d="M0 0 H360 V205 C250 232 120 200 0 182 Z" fill="url(#coverPhoto)"/>
    </svg>
    <p class="brand-name">Ventoro</p>
  </article>
</section>

<section class="spread spread--inner">
  <article class="page page--benefits">
    <svg class="page-art" viewBox="0 0 360 500" preserveAspectRatio="none" aria-hidden="true">
      <rect width="360" height="12" fill="var(--lime)"/>
      <path d="M0 470 C120 490 240 460 360 466 L360 500 L0 500 Z" fill="var(--lime)"/>
    </svg>
    <ul class="benefits">
      <li class="benefit"><span class="benefit-title">Build your own customers</span><span class="benefit-text">Riders you pick up can book you again directly.</span></li>
      <li class="benefit"><span class="benefit-title">Earn passive income</span><span class="benefit-text">Refer drivers and riders and earn on their trips.</span></li>
      <li class="benefit"><span class="benefit-title">Set your own hours</span><span class="benefit-text">Drive when it suits you, with no minimum shifts.</span></li>
      <li class="benefit"><span class="benefit-title">Fair, clear fares</span><span class="benefit-text">See what you earn before you accept a job.</span></li>
      <li class="benefit"><span class="benefit-title">Lower service fees</span><span class="benefit-text">Keep more of every fare than on other apps.</span></li>
      <li class="benefit"><span class="benefit-title">Local community</span><span class="benefit-text">Join drivers in your city who share tips and work.</span></li>
      <li class="benefit"><span class="benefit-title">Quick payouts</span><span class="benefit-text">Earnings reach your account every week.</span></li>
      <li class="benefit"><span class="benefit-title">Support when you need it</span><span class="benefit-text">Real people help you on and off the road.</span></li>
    </ul>
  </article>

  <article class="page page--jobs">
    <svg class="page-art" viewBox="0 0 360 500" preserveAspectRatio="none" aria-hidden="true">
      <rect width="360" height="12" fill="var(--lime)"/>
      <path d="M0 466 C120 460 240 490 360 470 L360 500 L0 500 Z" fill="var(--lime)"/>
    </svg>
    <h2 class="jobs-title">How we distribute jobs</h2>
    <p class="jobs-label">Booking Channel</p>
    <svg class="funnel" viewBox="0 0 190 200" aria-label="Job distribution funnel">
      <polygon points="0,0 190,0 173,36 0,36" fill="var(--blue-deep)"/>
      <polygon points="0,38 172,38 155,74 0,74" fill="var(--blue)"/>
      <polygon points="0,76 154,76 137,112 0,112" fill="var(--band-green)"/>
      <polygon points="0,114 136,114 119,150 0,150" fill="var(--band-orange)"/>
      <polygon points="0,152 118,152 95,200 0,200" fill="var(--band-red)"/>
      <text x="8" y="21">Your own clients</text>
      <text x="8" y="59">Referred clients</text>
      <text x="8" y="97">Local network</text>
      <text x="8" y="135">App bookings</text>
      <text x="8" y="173">Open jobs</text>
    </svg>
    <div class="people-figure" role="img" aria-label="Illustration of small people figures showing a growing referral network"></div>
    <p class="referral"><span>Refer your way to</span><strong>$200 / wk</strong><span>passive income</span></p>
    <p class="referral-note">Earn a share of every trip your referred drivers complete.</p>
  </article>
</section>

</body>
</html>
```